Startup company business card (Media & Advertising)

we need a business card design for a company that is a startup in the media and aggregation industry. Card needs to look funky and of a new breed/modern and upmarket.

Target Market(s)

advertisers/ brand agencies & media publishers

Industry/Entity Type

Advertising

Contact Information for Business Card

Please ensure the front face signifies our brand (plumvexo.com) and back has details for the contact. Standard contact such as phone , address, email , website etc.

Font styles to use
Other font styles liked:
• use styleguide and logo font and color

Colors

Designer to choose colors to be used in the design.

Requirements
Must have
• We are disrupting the media and agency industry so subtlety would be good to use imagery to signify this
Nice to have
• Please use logo colors for branding
Should not have
• be as creative and provide few options. Pick a brand color from logo and styleguide

```html
<!DOCTYPE html>
<html lang="en">
<head>
<meta charset="utf-8">
<title>plumvexo business card</title>
<link rel="stylesheet" href="https://fonts.googleapis.com/css2?family=Poppins:wght@400;600;700&display=swap">
<style>
  :root {
    --stage: #e4e4e4;
    --paper: #ffffff;
    --ink: #1e1e1e;
    --card-dark: #1b1b1b;
    --brand-red: #e8333b;
    --brand-deep: #b01e34;
    --edge-red: #9b1026;
    --text-grey: #3a3a3a;
  }
  * { box-sizing: border-box; margin: 0; padding: 0; }
  html, body {
    width: 1200px; height: 800px; overflow: hidden;
    background: var(--stage);
    font-family: "Poppins", sans-serif;
  }
  .stage { position: relative; width: 1200px; height: 800px; }

  .card {
    position: absolute;
    width: 540px; height: 310px;
    border-bottom: 4px solid var(--edge-red);
    border-radius: 2px;
    overflow: hidden;
  }

  /* Contact side */
  .card-contact { left: 50px; top: 110px; background: var(--paper); }
  .brand-shape {
    position: absolute; left: -120px; bottom: -170px;
    width: 380px; height: 380px;
  }
  .person { position: absolute; left: 300px; top: 34px; }
  .person-name { color: var(--brand-red); font-weight: 600; font-size: 24px; line-height: 1.1; }
  .person-role { color: var(--ink); font-size: 14px; margin-top: 2px; }
  .details { position: absolute; left: 300px; top: 150px; color: var(--text-grey); font-size: 13px; line-height: 1.6; }
  .details li { list-style: none; display: flex; align-items: center; gap: 8px; }
  .details .plain { padding-left: 0; }
  .icon { width: 12px; height: 12px; flex: none; }

  /* Brand side */
  .card-brand { left: 610px; top: 380px; background: var(--card-dark); }
  .wordmark {
    position: absolute; left: 0; right: 0; top: 50%;
    transform: translateY(-50%);
    display: flex; align-items: center; justify-content: center; gap: 18px;
  }
  .wordmark-dot { width: 40px; height: 40px; border-radius: 50%; background: var(--brand-red); }
  .wordmark-name { color: var(--paper); font-weight: 700; font-size: 54px; letter-spacing: 0.5px; }
</style>
</head>
<body>
<main class="stage">

  <section class="card card-contact">
    <svg class="brand-shape" viewBox="0 0 380 380" role="img" aria-label="Large red brand colour field">
      <defs>
        <linearGradient id="redField" x1="0" y1="0" x2="1" y2="1">
          <stop offset="0" stop-color="#ef3a40"/>
          <stop offset="1" stop-color="#b01e34"/>
        </linearGradient>
      </defs>
      <circle cx="190" cy="190" r="190" fill="url(#redField)"/>
    </svg>

    <div class="person">
      <p class="person-name">Daniel Harlow</p>
      <p class="person-role">President</p>
    </div>

    <ul class="details">
      <li class="plain">4218 Willow Bend Road</li>
      <li class="plain">Juneau, Alaska 99801</li>
      <li>
        <svg class="icon" viewBox="0 0 12 12" aria-hidden="true"><path d="M3 1 L5 3.5 L4 5 Q5 7 7 8 L8.5 7 L11 9 L9.5 11 Q4 10.5 1 2.5 Z" fill="var(--brand-red)"/></svg>
        555-014-2736
      </li>
      <li>
        <svg class="icon" viewBox="0 0 12 12" aria-hidden="true"><rect x="0.5" y="2" width="11" height="8" rx="1" fill="var(--brand-red)"/><path d="M1 2.5 L6 6.5 L11 2.5" stroke="#fff" stroke-width="1" fill="none"/></svg>
        info@plumvexo.com
      </li>
      <li>
        <svg class="icon" viewBox="0 0 12 12" aria-hidden="true"><circle cx="6" cy="6" r="5.5" fill="var(--brand-red)"/><path d="M0.5 6 H11.5 M6 0.5 Q3 6 6 11.5 M6 0.5 Q9 6 6 11.5" stroke="#fff" stroke-width="0.8" fill="none"/></svg>
        www.plumvexo.com
      </li>
    </ul>
  </section>

  <section class="card card-brand">
    <div class="wordmark">
      <span class="wordmark-dot"></span>
      <span class="wordmark-name">plumvexo</span>
    </div>
  </section>

</main>
</body>
</html>
```